Private Investigator needs a business card.

I am unsure of specifically what I want in regard to the design. You will find my company logo attached.

Please keep in mind. I cannot come across as a joke to people. My main clint bases is attorneys. I am not cheap to hire! Thus, I do not want to come across as cheap.

My information for the card:

Colin Ashworth, M.A.

Office 740.512.6043

eFax 740.236.1578

P.O. Box 417 
Corvane, Iowa 45102

DravikGrp.com

Civil and Criminal Cases Accepted

Target Market(s)

attorneys

Industry/Entity Type

Business

Contact Information for Business Card

Colin Ashworth, M.A.

Office 740.512.6043

eFax 740.236.1578

P.O. Box 417 
Corvane, Iowa 45102

DravikGrp.com

Requirements
Must have
• Include logo

```html
<!DOCTYPE html>
<html lang="en">
<head>
<meta charset="UTF-8">
<title>Dravik Group Ltd. — Business Card</title>
<link rel="stylesheet" href="https://fonts.googleapis.com/css2?family=Open+Sans:wght@400;600;700&family=Cormorant+Garamond:ital,wght@1,500&display=swap">
<style>
  :root {
    --backdrop: #3b322d;
    --card-dark: #151515;
    --card-light: #c9cacb;
    --ink-dark: #1c1c1c;
    --ink-mid: #4a4a4a;
    --silver: #b9b9b9;
    --silver-dim: #8c8c8c;
  }
  * { margin: 0; padding: 0; box-sizing: border-box; }
  html, body {
    width: 1200px; height: 787px; overflow: hidden;
    background: var(--backdrop);
  }
  .canvas {
    position: relative; width: 1200px; height: 787px;
    display: flex; align-items: center; justify-content: center; gap: 50px;
  }
  .card {
    width: 530px; height: 305px; position: relative;
    box-shadow: 0 10px 28px rgba(0,0,0,.45);
  }
  /* Front */
  .card--front {
    background: var(--card-dark); color: var(--silver);
    display: flex; flex-direction: column; align-items: center; justify-content: center;
  }
  .brand { display: flex; flex-direction: column; align-items: center; }
  .brand__row { display: flex; align-items: center; gap: 12px; }
  .brand__mark { width: 18px; height: 18px; background: currentColor; }
  .brand__name {
    font-family: "Open Sans", sans-serif; font-weight: 700;
    font-size: 27px; letter-spacing: 1.5px; text-transform: uppercase;
  }
  .brand__tagline {
    font-family: "Open Sans", sans-serif; font-weight: 600;
    font-size: 8.5px; letter-spacing: .8px; text-transform: uppercase;
    margin-top: 5px; padding-top: 4px; border-top: 1px solid currentColor;
  }
  .front__top-rule {
    width: 440px; height: 1px; background: var(--silver-dim); margin-top: 26px;
  }
  .front__rule {
    display: flex; align-items: center; gap: 14px; margin-top: 34px;
    width: 440px; color: var(--silver-dim);
  }
  .front__rule::before, .front__rule::after {
    content: ""; flex: 1; height: 1px; background: currentColor;
  }
  .front__rule span {
    font-family: "Cormorant Garamond", serif; font-style: italic; font-weight: 500;
    font-size: 19px; color: var(--silver); white-space: nowrap;
  }
  /* Back */
  .card--back {
    background: var(--card-light); color: var(--ink-dark);
    display: flex; align-items: center;
  }
  .back__brand {
    width: 290px; display: flex; justify-content: center; color: var(--ink-dark);
  }
  .back__brand .brand__name { font-size: 20px; letter-spacing: 1px; }
  .back__brand .brand__mark { width: 14px; height: 14px; }
  .back__brand .brand__tagline { font-size: 6.5px; }
  .back__divider { width: 1px; height: 180px; background: var(--ink-mid); opacity: .6; }
  .contact {
    padding-left: 26px; font-family: "Open Sans", sans-serif; color: var(--ink-mid);
    font-size: 13.5px; line-height: 1.45;
  }
  .contact__name { font-weight: 700; font-size: 15.5px; color: var(--ink-dark); margin-bottom: 8px; }
  .contact__address { margin-bottom: 8px; }
  .contact__line { display: flex; align-items: center; gap: 8px; }
  .contact__line svg { width: 13px; height: 13px; fill: var(--ink-dark); flex: none; }
</style>
</head>
<body>
<main class="canvas">
  <section class="card card--front" aria-label="Card front">
    <div class="brand">
      <div class="brand__row">
        <span class="brand__mark"></span>
        <span class="brand__name">Dravik Group Ltd.</span>
      </div>
      <span class="brand__tagline">A Private Investigation and Analysis Firm</span>
    </div>
    <div class="front__top-rule"></div>
    <div class="front__rule"><span>Civil and Criminal Cases Accepted</span></div>
  </section>

  <section class="card card--back" aria-label="Card back">
    <div class="back__brand">
      <div class="brand">
        <div class="brand__row">
          <span class="brand__mark"></span>
          <span class="brand__name">Dravik Group Ltd.</span>
        </div>
        <span class="brand__tagline">A Private Investigation and Analysis Firm</span>
      </div>
    </div>
    <div class="back__divider"></div>
    <div class="contact">
      <p class="contact__name">Colin Ashworth, M.A.</p>
      <p class="contact__address">P.O. Box 417<br>Corvane, Iowa 45102</p>
      <p class="contact__line">
        <svg viewBox="0 0 16 16" aria-hidden="true"><path d="M3 2c1-1 2-1 3 0l1.5 2c.5.8.3 1.5-.3 2l-1 .8c.7 1.5 2 2.8 3.5 3.5l.8-1c.5-.6 1.2-.8 2-.3l2 1.5c1 1 1 2 0 3-1.5 1.5-4 1-7-2S1.5 3.5 3 2z"/></svg>
        555.512.6043
      </p>
      <p class="contact__line">
        <svg viewBox="0 0 16 16" aria-hidden="true"><rect x="4" y="1" width="8" height="5"/><rect x="1" y="6" width="14" height="6" rx="1"/><rect x="4" y="11" width="8" height="4"/></svg>
        555.236.1578
      </p>
      <p class="contact__line">
        <svg viewBox="0 0 16 16" aria-hidden="true"><path d="M8 1a7 7 0 1 0 0 14A7 7 0 0 0 8 1zm-5.4 6.2h2.4c.1-1.6.4-3 1-4a5.6 5.6 0 0 0-3.4 4zm3.9 0h3c-.1-2-.8-3.9-1.5-4.3-.7.4-1.4 2.3-1.5 4.3zm4.5 0h2.4a5.6 5.6 0 0 0-3.4-4c.6 1 .9 2.4 1 4zm-8.4 1.6a5.6 5.6 0 0 0 3.4 4c-.6-1-.9-2.4-1-4zm3.9 0c.1 2 .8 3.9 1.5 4.3.7-.4 1.4-2.3 1.5-4.3zm4.5 0c-.1 1.6-.4 3-1 4a5.6 5.6 0 0 0 3.4-4z"/></svg>
        www.DravikGrp.com
      </p>
    </div>
  </section>
</main>
</body>
</html>
```